Photojournalism/photography business needs a simple, timeless & professional letterhead design

We need a letterhead design for photography/photojournalism business called 'qolvb', no capitals.

The letterhead needs to be:
- simple
- professional
- timeless
- easy to read
- consists of at least 2 colors to make it stands out.

We do mainly editorial photography, photo articles for various publications, travel, businesses, as well as people such as family and kids.

The final design should communicate professionalism, easy identification, attention grabbing, even if it has to be found among a stack of various papers on the clients' desks.

Target Market(s)

Various publications.

Industry/Entity Type

Business

Requirements
Must have
• Please use the logo attached.

```html
<!DOCTYPE html>
<html lang="en">
<head>
<meta charset="utf-8">
<title>qolvb letterhead</title>
<link rel="stylesheet" href="https://fonts.googleapis.com/css2?family=Montserrat:wght@500;700&display=swap">
<style>
  :root {
    --ink-dark: #38383a;
    --ink-grey: #3e3e40;
    --ink-light: #b9b9bb;
    --paper: #ffffff;
  }
  html, body {
    margin: 0;
    padding: 0;
    overflow: hidden;
    background: var(--paper);
  }
  .letterhead {
    position: relative;
    width: 900px;
    height: 1200px;
    background: var(--paper);
    overflow: hidden;
    font-family: "Montserrat", sans-serif;
  }
  .corner-curve {
    position: absolute;
    inset: 0;
  }
  .corner-curve path {
    fill: var(--ink-dark);
  }
  .brand-name {
    position: absolute;
    left: 0;
    width: 850px;
    text-align: center;
    margin: 0;
    font-weight: 700;
    letter-spacing: 1px;
    line-height: 1;
  }
  .brand-name--header {
    top: 38px;
    font-size: 44px;
    color: var(--ink-dark);
  }
  .brand-name--footer {
    top: 1060px;
    font-size: 40px;
    color: var(--ink-light);
  }
  .sender-details {
    position: absolute;
    left: 0;
    top: 1120px;
    width: 850px;
    margin: 0;
    text-align: center;
    font-style: normal;
    font-weight: 500;
    font-size: 22px;
    line-height: 22px;
    letter-spacing: 1px;
    color: var(--ink-grey);
  }
</style>
</head>
<body>
  <main class="letterhead">
    <svg class="corner-curve" width="900" height="1200" viewBox="0 0 900 1200" aria-hidden="true">
      <path d="M0 0 H210 C120 10 50 80 0 170 Z"/>
      <path d="M900 1200 H722 C820 1160 880 1110 900 1020 Z"/>
    </svg>

    <p class="brand-name brand-name--header">qolvb</p>

    <p class="brand-name brand-name--footer">qolvb</p>
    <address class="sender-details">
      Your Name<br>
      Your Address<br>
      Your Contact Details
    </address>
  </main>
</body>
</html>
```